I would Like a design for our company's Elderflower Vodka. It is 70cl bottle, ( image of bottle attached) It will be 37.5% vol.The label would be nice to include a tasteful classy floral theme

```html
<!DOCTYPE html>
<html lang="en">
<head>
<meta charset="utf-8">
<title>Elderflower Vodka Label</title>
<link rel="stylesheet" href="https://fonts.googleapis.com/css2?family=Barlow+Condensed:wght@600&family=Playfair+Display:ital,wght@0,400;1,400&display=swap">
<style>
  :root {
    --page: #ffffff;
    --label-cream: #eeeadc;
    --panel: rgba(249, 248, 244, 0.86);
    --frame-line: rgba(255, 255, 255, 0.75);
    --ink: #3a3a38;
    --brand-red: #7a1f26;
    --flower-dark: #a9aaa0;
    --flower-light: #d8d8cf;
  }
  * { margin: 0; padding: 0; box-sizing: border-box; }
  html, body {
    width: 1173px;
    height: 1200px;
    overflow: hidden;
    background: var(--page);
  }
  .canvas {
    position: relative;
    width: 1173px;
    height: 1200px;
  }
  .label {
    position: absolute;
    left: 144px;
    top: 48px;
    width: 888px;
    height: 1100px;
    background: var(--label-cream);
    overflow: hidden;
  }
  .flower-area {
    position: absolute;
    left: -10px;
    top: 150px;
    width: 840px;
    height: 820px;
    background:
      radial-gradient(ellipse 38% 30% at 62% 62%, var(--flower-dark), transparent 75%),
      radial-gradient(ellipse 45% 25% at 45% 22%, var(--flower-dark), transparent 75%),
      radial-gradient(ellipse 60% 50% at 50% 45%, var(--flower-light), transparent 80%);
    opacity: 0.85;
  }
  .brand {
    position: absolute;
    left: 0;
    right: 0;
    top: 88px;
    text-align: center;
    font-family: "Playfair Display", serif;
    font-weight: 400;
    font-size: 24px;
    letter-spacing: 4px;
    text-transform: uppercase;
    color: var(--brand-red);
  }
  .frame {
    position: absolute;
    left: 107px;
    top: 319px;
    width: 674px;
    height: 642px;
    border: 4px solid var(--frame-line);
  }
  .panel {
    position: absolute;
    left: 127px;
    top: 337px;
    width: 635px;
    height: 605px;
    background: var(--panel);
  }
  .product-name {
    position: absolute;
    left: 0;
    right: 0;
    top: 228px;
    text-align: center;
    font-family: "Barlow Condensed", sans-serif;
    font-weight: 600;
    font-size: 122px;
    line-height: 1;
    letter-spacing: -1px;
    color: var(--ink);
  }
  .product-type {
    position: absolute;
    left: 0;
    right: 0;
    top: 342px;
    text-align: center;
    font-family: "Playfair Display", serif;
    font-style: italic;
    font-size: 58px;
    line-height: 1;
    color: var(--ink);
  }
  .spec {
    position: absolute;
    top: 552px;
    font-family: "Playfair Display", serif;
    font-style: italic;
    font-size: 29px;
    line-height: 1;
    color: var(--ink);
    letter-spacing: -1px;
  }
  .spec--abv { left: 8px; }
  .spec--volume { right: 20px; }
</style>
</head>
<body>
  <div class="canvas">
    <div class="label">
      <div class="flower-area" role="img" aria-label="Soft-focus photograph of an elderflower blossom cluster"></div>
      <div class="brand">Hollow Lane Spirit Co.</div>
      <div class="frame"></div>
      <div class="panel">
        <h1 class="product-name">ELDERFLOWER</h1>
        <p class="product-type">Vodka</p>
        <p class="spec spec--abv">37,5%</p>
        <p class="spec spec--volume">70cl</p>
      </div>
    </div>
  </div>
</body>
</html>
```